Web Application Graphic Design Project

We need a design for an online literacy application. The target audience are 9-12 year old children and the application will teach them literacy skills, like essay writing. It is a web-based application called Lumorival and the software developers now need a graphic design to implement into the code - no coding required, just design of the layout.
Wireframes are attached to give an overview of what the functionalities are - it runs in any ordinary web-browser (indicated in the wireframes as well). The application consists of a static background (workspace) onto which individual boxes are added as the student progresses through the tasks. A task panel on the left hand side allows the user to select a task, upon which a popup window will slide open on the right where they enter content. This content is then displayed on the workspace in the background in a box (which can be moved around to organise, seen in frame 3 ). Additional icons on left and right lead to new tasks.
Updates
The wireframe mockup of the application has been updated - please ignore the previous one, which has now been deleted. This is the final version to work from.
Reason: Would like to give more time to allow for a design that meets the young children target audience and for more creative ways for icons and colour schemes.
Reason: We are waiting for some further submissions to come through.
Target Market(s)
9-12 year old school children, so the design should be appealing to both boys and girls.
Industry/Entity Type
Graphic Design
Look and feel
Each slider illustrates characteristics of the customer's brand and the style your logo design should communicate.

```html
<!DOCTYPE html>
<html lang="en">
<head>
<meta charset="utf-8">
<title>Lumorival – Essay Writing</title>
<link rel="stylesheet" href="https://fonts.googleapis.com/css2?family=PT+Sans:wght@400;700&display=swap">
<style>
  :root{
    --bg:#f4f4f4;
    --panel:#ffffff;
    --line:#cfcfcf;
    --line-dark:#a9a9a9;
    --ink:#111111;
    --ink-soft:#333333;
    --muted:#b5b5b5;
    --orange:#f0a030;
    --orange-dark:#c97a10;
    --green:#43b02a;
    --red:#d42525;
    --blue:#3a78c8;
    --gold:#ffcc1a;
  }
  *{box-sizing:border-box;margin:0;padding:0}
  html,body{width:1200px;height:779px;overflow:hidden;background:var(--bg)}
  body{font-family:"PT Sans",Arial,sans-serif;color:var(--ink)}
  .stage{position:relative;width:1280px;height:831px;transform:scale(.9375);transform-origin:0 0}
  .abs{position:absolute}

  .tool{position:absolute;width:70px;text-align:center;font-size:11px;color:var(--ink)}
  .tool svg{display:block;margin:0 auto 2px}

  .task-panel{left:78px;top:51px;width:256px;height:736px;background:var(--panel);border:1px solid #dcdcdc;box-shadow:0 0 4px rgba(0,0,0,.12)}
  .level{position:absolute;top:14px;width:70px;text-align:center;font-size:11px}
  .level svg,.level .level-mark{display:block;margin:0 auto 4px;height:38px}
  .level-mark{font-weight:700;font-size:40px;line-height:38px}
  .panel-title{position:absolute;left:11px;top:90px;font-size:22px;letter-spacing:.2px}
  .task-list{position:absolute;left:32px;top:128px;list-style:none;font-size:15px}
  .task-list li{height:29.6px;position:relative;width:190px}
  .task-list svg{position:absolute;right:-4px;top:-2px}

  .teacher-box{left:352px;top:160px;width:330px;height:124px;border:2px solid #555;background:var(--panel)}
  .teacher-box .legend{position:absolute;left:34px;top:-14px;background:var(--panel);padding:0 2px;font-size:22px;line-height:26px}
  .teacher-box p{position:absolute;left:17px;top:16px;font-size:21px;line-height:28px;width:300px}

  .popup{left:475px;top:51px;width:686px;height:596px;background:var(--panel);border:1px solid #d6d6d6;box-shadow:0 0 5px rgba(0,0,0,.15)}
  .popup-title{position:absolute;left:8px;top:8px;font-size:20px}
  .win-controls{position:absolute;right:12px;top:10px}
  .popup-body{position:absolute;left:5px;top:48px;width:675px;height:541px;border:1px solid var(--line-dark)}
  .reader{position:absolute;left:21px;top:10px;width:484px;height:519px;border:1px solid var(--line-dark)}
  .reader h2{font-weight:400;font-size:19px;text-align:center;margin-top:6px}
  .reader-text{position:absolute;left:5px;top:60px;width:475px;font-size:14.5px;line-height:19px}
  .reader-foot{position:absolute;left:0;bottom:0;width:100%;height:34px;border-top:1px solid var(--line-dark);text-align:right;padding:6px 8px 0 0;font-size:14px}
  .reader-foot svg{vertical-align:-3px;margin-left:4px}
  .marker{position:absolute;left:2px;width:16px;height:17px;background:var(--orange);border:1px solid var(--orange-dark);border-radius:2px;color:#fff;font-size:10px;text-align:center;line-height:15px}
  .marker::after{content:"";position:absolute;right:-5px;top:4px;border:4px solid transparent;border-left-color:var(--orange-dark);border-right:0}

  .notes{position:absolute;left:512px;top:0;width:162px;height:539px;border-left:1px solid var(--line-dark)}
  .note{position:relative;border-bottom:1px solid var(--line-dark);font-size:14px;line-height:19px;padding-left:11px}
  .note .close{position:absolute;right:8px;top:5px}
  .note .hang{padding-left:16px;text-indent:-16px}
</style>
</head>
<body>
<div class="stage">

  <!-- left tools -->
  <div class="tool" style="left:0;top:74px">
    <svg width="42" height="40" viewBox="0 0 42 40"><polygon points="6,36 9,26 32,3 39,10 16,33" fill="#f6b53a" stroke="#b07818"/><polygon points="6,36 9,26 16,33" fill="#f3d6a4"/><polygon points="6,36 7.5,31 11,34.5" fill="#333"/><polygon points="32,3 39,10 36,13 29,6" fill="#e26a6a"/></svg>
    Lesson
  </div>
  <div class="tool" style="left:0;top:163px">
    <svg width="46" height="44" viewBox="0 0 46 44"><rect x="4" y="3" width="38" height="38" rx="3" fill="#2f3a45"/><path d="M9 8h13v28H9zM24 8h13v28H24z" fill="#fff"/><rect x="21" y="6" width="4" height="32" fill="#2f3a45"/><polygon points="27,8 31,8 31,16 29,14 27,16" fill="#2f3a45"/></svg>
    Activities
  </div>

  <!-- task panel -->
  <section class="abs task-panel">
    <div class="level" style="left:16px"><span class="level-mark">B</span>Newbie</div>
    <div class="level" style="left:97px">
      <svg width="40" height="38" viewBox="0 0 40 38"><polygon points="4,32 24,12 16,12 16,4 36,4 36,24 28,24 28,16 8,36" fill="var(--blue)" stroke="#24569a"/></svg>
      Developer
    </div>
    <div class="level" style="left:178px">
      <svg width="40" height="38" viewBox="0 0 40 38"><polygon points="20,2 25,14 38,14.5 28,23 31.5,36 20,28.5 8.5,36 12,23 2,14.5 15,14" fill="var(--gold)" stroke="#d9a000"/></svg>
      Star
    </div>
    <h1 class="panel-title" style="font-weight:400">ESSAY WRITING</h1>
    <ul class="task-list">
      <li>Overview</li>
      <li>The Question<svg width="26" height="24" viewBox="0 0 26 24"><path d="M2 13l5-4 5 6L23 2l3 3-14 17z" fill="var(--green)"/></svg></li>
      <li>Decoding the Q<svg width="26" height="24" viewBox="0 0 26 24"><path d="M2 13l5-4 5 6L23 2l3 3-14 17z" fill="var(--green)"/></svg></li>
      <li>Your Ideas<svg width="26" height="24" viewBox="0 0 26 24"><path d="M2 13l5-4 5 6L23 2l3 3-14 17z" fill="var(--green)"/></svg></li>
      <li>Structure</li>
      <li>Writing</li>
      <li>Review</li>
    </ul>
  </section>

  <!-- workspace box -->
  <div class="abs teacher-box">
    <span class="legend">Teacher-set question</span>
    <p>How has the internet changed our perception of information?</p>
  </div>

  <!-- popup -->
  <section class="abs popup">
    <div class="popup-title">Chasing My Tail</div>
    <svg class="win-controls" width="56" height="16" viewBox="0 0 56 16"><rect x="1" y="9" width="12" height="3" fill="var(--muted)"/><rect x="22" y="4" width="11" height="10" fill="none" stroke="var(--muted)" stroke-width="2"/><rect x="25" y="1" width="11" height="10" fill="none" stroke="var(--muted)" stroke-width="2"/><path d="M43 2l12 12M55 2L43 14" stroke="var(--muted)" stroke-width="3"/></svg>

    <div class="popup-body">
      <article class="reader">
        <h2>CHASING MY TAIL</h2>
        <p class="reader-text">This is a sample text that students can read.<br>Texts are also annotated. These annotations give students information about the text.<br>Each annotation has a number, Annotations appear only when it’s number is clicked. The annotation appears on the right side in order.<br>The X’s on the right indicate “Close” icons for each annotation</p>
        <div class="reader-foot">57<svg width="20" height="18" viewBox="0 0 20 18"><rect x="1" y="7" width="4" height="10" fill="var(--green)"/><path d="M6 8l4-7c2 0 2 2 1.5 5H18c1 0 1.5 1 1 2l-2 8c-.3 1-1 1-2 1H6z" fill="var(--green)"/></svg></div>
      </article>
      <span class="marker" style="top:77px">1</span>
      <span class="marker" style="top:128px">2</span>
      <span class="marker" style="top:151px">3</span>

      <aside class="notes">
        <div class="note" style="height:87px;padding-top:37px"><svg class="close" width="18" height="18" viewBox="0 0 18 18"><circle cx="9" cy="9" r="8" fill="var(--red)"/><path d="M5.5 5.5l7 7M12.5 5.5l-7 7" stroke="#fff" stroke-width="2"/></svg><p class="hang">1. This is the first sentence.</p></div>
        <div class="note" style="height:101px;padding-top:50px"><svg class="close" width="18" height="18" viewBox="0 0 18 18"><circle cx="9" cy="9" r="8" fill="var(--red)"/><path d="M5.5 5.5l7 7M12.5 5.5l-7 7" stroke="#fff" stroke-width="2"/></svg><p class="hang">2. Information about 2 is here.</p></div>
        <div class="note" style="height:77px;padding-top:47px"><svg class="close" width="18" height="18" viewBox="0 0 18 18"><circle cx="9" cy="9" r="8" fill="var(--red)"/><path d="M5.5 5.5l7 7M12.5 5.5l-7 7" stroke="#fff" stroke-width="2"/></svg><p>3. More information</p></div>
      </aside>
    </div>
  </section>

  <!-- right tools -->
  <div class="tool" style="left:1199px;top:14px">
    <svg width="40" height="42" viewBox="0 0 40 42"><path d="M4 42c0-12 7-17 16-17s16 5 16 17z" fill="#e8641e"/><circle cx="20" cy="14" r="10" fill="#f2b27a"/><path d="M10 12c0-7 5-10 10-10s10 3 10 10c-3-3-8-4-20 0z" fill="#3a2a1a"/></svg>
    My Name
  </div>
  <div class="tool" style="left:1199px;top:101px">
    <svg width="38" height="38" viewBox="0 0 38 38"><circle cx="19" cy="19" r="17" fill="#3d8fd6" stroke="#2a6aa8"/><path d="M8 12c4 0 6 3 9 2s2 6-2 7-3 6-6 5c-3-4-4-10-1-14zM22 6c4 1 9 5 10 11-3 0-4-3-7-2s-3-5-3-9z" fill="#8cc8f0"/></svg>
    Reference
  </div>
  <div class="tool" style="left:1199px;top:181px">
    <svg width="36" height="40" viewBox="0 0 36 40"><path d="M4 2h20l8 8v28H4z" fill="#fff" stroke="#7a9cc8" stroke-width="2"/><rect x="2" y="12" width="22" height="18" fill="#4a7fc4"/><path d="M24 2v8h8" fill="#dbe6f4" stroke="#7a9cc8" stroke-width="2"/></svg>
    Samples
  </div>
  <div class="tool" style="left:1199px;top:262px">
    <svg width="38" height="42" viewBox="0 0 38 42"><rect x="4" y="14" width="30" height="26" rx="2" fill="#9ca3aa" stroke="#6b7278"/><rect x="9" y="14" width="20" height="10" fill="#e4e7ea"/><rect x="10" y="29" width="18" height="11" fill="#fff"/><polygon points="13,2 25,2 25,10 31,10 19,22 7,10 13,10" fill="#4cb848" stroke="#2f8a2b"/></svg>
    Save
  </div>
  <div class="tool" style="left:1199px;top:347px">
    <svg width="36" height="36" viewBox="0 0 36 36"><g fill="#a0a4a8" stroke="#6e7276"><circle cx="18" cy="18" r="11"/><rect x="15" y="1" width="6" height="8"/><rect x="15" y="27" width="6" height="8"/><rect x="1" y="15" width="8" height="6"/><rect x="27" y="15" width="8" height="6"/><rect x="15" y="1" width="6" height="8" transform="rotate(45 18 18)"/><rect x="15" y="27" width="6" height="8" transform="rotate(45 18 18)"/><rect x="1" y="15" width="8" height="6" transform="rotate(45 18 18)"/><rect x="27" y="15" width="8" height="6" transform="rotate(45 18 18)"/></g><circle cx="18" cy="18" r="5" fill="#fff" stroke="#6e7276"/></svg>
    Settings
  </div>
  <div class="tool" style="left:1199px;top:427px">
    <svg width="36" height="36" viewBox="0 0 36 36"><path d="M3 8l5-5 10 10L28 3l5 5-10 10 10 10-5 5-10-10L8 33l-5-5 10-10z" fill="var(--red)" stroke="#9a1515"/></svg>
    Exit
  </div>

</div>
</body>
</html>
```